Facebook Post for Fence Spring Sale

We have a $12 / FT Fence sale that we have been running for a while now. We need a flyer made up for SPRING.

Our previous flyer can be seen here:
https://media.pixvault-host.example/img/48213907_551903288146720_7391026458813302947_n.jpg?ref=7c21b9e04d8a

We want to use the photos that are shown here https://files.cloudtrove-share.example/view?id=9XkQ7rTmw2LpZdVa4HsE in the flyer. This is to be posted on Facebook so it must be the proper size for Facebook page post.

The wording to be used should be "Spring Fence Sale" and "$12 / FT Wood Fences" Also we should include our business name "Oakridge Fence" and phone number for Free Estimates - 555-314-2076.

Residential Construction

Font styles to use
Serif
Sans Serif

Colors
3176b5
fbee3d
fbed22
fbf289
85cae6
33a6d7

Requirements
Must have
• Phone number, $12 / FT Fence Sale

```html
<!DOCTYPE html>
<html lang="en">
<head>
<meta charset="utf-8">
<title>Spring Fence Sale – Oakridge Fence</title>
<link rel="stylesheet" href="https://fonts.googleapis.com/css2?family=Great+Vibes&family=Open+Sans:wght@400;600;700;800&display=swap">
<style>
  :root {
    --teal: #4ba4b8;
    --teal-dark: #3f95a8;
    --sky-wash: #d7ebf5;
    --paper: #f7fbfd;
    --tag-red: #d9615d;
    --ribbon-green: #2e8b45;
    --frame-dark: #2b2321;
    --wood-light: #e2c99a;
    --wood-mid: #c9a571;
    --string-grey: #9aa3a8;
    --white: #ffffff;
  }
  * { box-sizing: border-box; margin: 0; padding: 0; }
  html, body { width: 1200px; height: 1200px; overflow: hidden; }
  body { background: var(--white); }

  .post {
    position: relative;
    width: 1200px;
    height: 1200px;
    overflow: hidden;
    background: radial-gradient(ellipse at 55% 45%, var(--paper) 0%, #eaf4f9 55%, var(--sky-wash) 100%);
  }

  /* watercolour floral borders */
  .floral { position: absolute; border-radius: 50%; filter: blur(2px); opacity: .85; }
  .floral--top-left { left: -90px; top: -90px; width: 300px; height: 360px;
    background: radial-gradient(circle at 60% 60%, rgba(63,155,106,.55), rgba(239,106,58,.25) 55%, transparent 72%); }
  .floral--top { left: 280px; top: -130px; width: 520px; height: 200px;
    background: radial-gradient(ellipse at 50% 40%, rgba(63,155,106,.4), rgba(111,166,214,.28) 50%, transparent 72%); }
  .floral--top-right { right: -110px; top: -80px; width: 300px; height: 420px;
    background: radial-gradient(circle at 40% 55%, rgba(243,166,160,.7), rgba(63,155,106,.35) 50%, transparent 72%); }
  .floral--right { right: -90px; top: 360px; width: 230px; height: 560px;
    background: radial-gradient(ellipse at 45% 50%, rgba(111,166,214,.55), rgba(63,155,106,.35) 50%, transparent 72%); }
  .floral--left { left: -110px; top: 430px; width: 260px; height: 540px;
    background: radial-gradient(ellipse at 55% 45%, rgba(243,120,120,.6), rgba(63,155,106,.4) 50%, transparent 72%); }
  .floral--bottom { left: 0; bottom: -120px; width: 1200px; height: 230px;
    background: radial-gradient(ellipse at 50% 60%, rgba(63,155,106,.45), rgba(243,140,140,.3) 45%, transparent 72%); }

  /* headline */
  .headline-sale {
    position: absolute;
    left: 110px;
    top: 105px;
    font-family: 'Great Vibes', cursive;
    font-size: 460px;
    line-height: 1;
    color: var(--teal);
    text-shadow: 4px 6px 0 var(--white), 8px 14px 18px rgba(80,110,130,.25);
    letter-spacing: -4px;
  }
  .headline-season {
    position: absolute;
    left: 408px;
    top: 180px;
    font-family: 'Great Vibes', cursive;
    font-size: 76px;
    line-height: 1;
    color: var(--teal);
    text-shadow:
      0 0 6px var(--white), 0 0 10px var(--white), 0 0 14px var(--white),
      3px 3px 0 var(--white), -3px -3px 0 var(--white), 3px -3px 0 var(--white), -3px 3px 0 var(--white);
  }

  /* price tag */
  .price-tag {
    position: absolute;
    left: 92px;
    top: 540px;
    width: 260px;
    height: 350px;
    transform: rotate(-11deg);
    transform-origin: 50% 0;
  }
  .price-tag__card {
    position: absolute;
    inset: 0;
    background: var(--tag-red);
    border: 10px solid var(--white);
    border-radius: 26px;
    box-shadow: 4px 8px 18px rgba(0,0,0,.15);
  }
  .price-tag__hole {
    position: absolute;
    left: 50%; top: 30px;
    width: 30px; height: 30px;
    margin-left: -15px;
    border-radius: 50%;
    background: var(--white);
  }
  .price-tag__ribbon {
    position: absolute;
    left: 10px; right: 10px; top: 84px;
    height: 22px;
    background: var(--ribbon-green);
  }
  .price-tag__bow {
    position: absolute;
    left: 50%; top: 70px;
    width: 92px; height: 50px;
    margin-left: -46px;
    border-radius: 40%;
    background: radial-gradient(ellipse, #3aa055, var(--ribbon-green));
  }
  .price-tag__amount {
    position: absolute;
    left: 0; right: 0; top: 150px;
    text-align: center;
    font-family: 'Open Sans', sans-serif;
    font-weight: 700;
    font-size: 36px;
    color: var(--white);
  }
  .price-tag__label {
    position: absolute;
    left: 0; right: 0; top: 200px;
    text-align: center;
    font-family: 'Great Vibes', cursive;
    font-size: 54px;
    line-height: .95;
    color: var(--white);
  }
  .price-tag__string { position: absolute; left: 0; top: 0; overflow: visible; }

  /* hanging gallery */
  .gallery-rail { position: absolute; left: 0; top: 0; overflow: visible; }
  .gallery-frame {
    position: absolute;
    background: var(--frame-dark);
    padding: 12px;
    box-shadow: 3px 8px 16px rgba(0,0,0,.22);
  }
  .gallery-frame__photo {
    width: 100%; height: 100%;
    border: 6px solid var(--white);
    background: linear-gradient(135deg, var(--wood-light), var(--wood-mid));
  }
  .gallery-frame--one   { left: 416px; top: 685px; width: 214px; height: 243px; }
  .gallery-frame--two   { left: 652px; top: 745px; width: 216px; height: 245px; }
  .gallery-frame--three { left: 905px; top: 685px; width: 214px; height: 243px; }
  .gallery-frame--two .gallery-frame__photo { background: linear-gradient(160deg, #4c6a35 0%, #4c6a35 30%, #efe2b6 31%, #d9c99a 100%); }

  /* brand and contact */
  .brand-name {
    position: absolute;
    left: 50px;
    top: 1020px;
    font-family: 'Great Vibes', cursive;
    font-size: 90px;
    line-height: 1;
    color: var(--teal-dark);
  }
  .contact {
    position: absolute;
    left: 756px;
    top: 1036px;
    font-family: 'Open Sans', sans-serif;
    color: var(--teal);
  }
  .contact__lead { font-size: 30px; font-weight: 400; line-height: 1.1; }
  .contact__phone { font-size: 60px; font-weight: 700; line-height: 1.1; letter-spacing: .5px; }
</style>
</head>
<body>
  <main class="post">
    <div class="floral floral--top-left" role="img" aria-label="Watercolour leaves and red berries"></div>
    <div class="floral floral--top" role="img" aria-label="Watercolour green and blue leaves"></div>
    <div class="floral floral--top-right" role="img" aria-label="Watercolour pink rose and leaves"></div>
    <div class="floral floral--right" role="img" aria-label="Watercolour blue leaves and butterflies"></div>
    <div class="floral floral--left" role="img" aria-label="Watercolour pink flower and orange blossoms"></div>
    <div class="floral floral--bottom" role="img" aria-label="Watercolour border of flowers and leaves"></div>

    <h1 class="headline">
      <span class="headline-sale">Sale</span>
      <span class="headline-season">Spring Fence</span>
    </h1>

    <div class="price-tag">
      <div class="price-tag__card"></div>
      <div class="price-tag__hole"></div>
      <div class="price-tag__ribbon"></div>
      <div class="price-tag__bow" role="img" aria-label="Green ribbon bow"></div>
      <p class="price-tag__amount">$12/ ft</p>
      <p class="price-tag__label">Wood<br>Fences</p>
    </div>

    <svg class="price-tag__string" width="1200" height="700" aria-hidden="true">
      <path d="M230 583 C 170 560, 110 500, 105 440 C 100 395, 125 380, 140 400 C 158 430, 180 500, 230 583"
            fill="none" stroke="var(--string-grey)" stroke-width="3" stroke-linecap="round"/>
    </svg>

    <svg class="gallery-rail" width="1200" height="760" aria-hidden="true">
      <g stroke="#4ba4b8" stroke-width="4" fill="#4ba4b8">
        <line x1="475" y1="546" x2="1200" y2="546"/>
        <circle cx="475" cy="546" r="6"/>
        <line x1="522" y1="546" x2="522" y2="640" stroke-width="2"/>
        <circle cx="522" cy="652" r="6"/>
        <line x1="760" y1="546" x2="760" y2="700" stroke-width="2"/>
        <circle cx="760" cy="714" r="6"/>
        <line x1="1010" y1="546" x2="1010" y2="640" stroke-width="2"/>
        <circle cx="1010" cy="652" r="6"/>
      </g>
    </svg>

    <figure class="gallery-frame gallery-frame--one">
      <div class="gallery-frame__photo" role="img" aria-label="Photo of a tall cedar privacy fence with a scalloped top"></div>
    </figure>
    <figure class="gallery-frame gallery-frame--two">
      <div class="gallery-frame__photo" role="img" aria-label="Photo of an arched picket fence on a lawn"></div>
    </figure>
    <figure class="gallery-frame gallery-frame--three">
      <div class="gallery-frame__photo" role="img" aria-label="Photo of a picket fence gate with black hinges"></div>
    </figure>

    <p class="brand-name">Oakridge Fence</p>

    <div class="contact">
      <p class="contact__lead">For Free Estmates</p>
      <p class="contact__phone">555-314-2076</p>
    </div>
  </main>
</body>
</html>
```